Telvan Flash Banner Ad

We require a flash banner ad for a new product of ours called Telvan (www.telvan.com.au). Telvan is a web-based system generating life insurance quotes using a widget embedded in your site.
The banner should have the following screens:
1. Life Insurance, Total & Permanent Disablement Insurance, Income Protection Insurance
2. No Blood Tests or Medicals Required.
3. Up to $1 million Cover with Leading Brands.
4. Click here for an Instant Quote.
We require the following sizes:
- 300 x 250
- 728 x 90
Life Insurance

```html
<!DOCTYPE html>
<html lang="en">
<head>
<meta charset="utf-8">
<title>Telvan Banner Colourways</title>
<link rel="stylesheet" href="https://fonts.googleapis.com/css2?family=Archivo:ital,wght@1,400;1,500;1,700;1,900&display=swap">
<style>
  :root {
    --page: #ffffff;
    --ink: #000000;
    --white: #ffffff;
    --frame: #1a1a1a;
    --powered: #3a8fb0;
    --brand-text: #555555;
    --brand-dot: #6cbf3a;
    --red-light: #d80a0a; --red-dark: #980000;
    --teal-light: #52bfd2; --teal-dark: #2a7d8c;
    --green-light: #55c46f; --green-dark: #2f8748;
    --purple-light: #bd80dc; --purple-dark: #7b4a95;
    --grey-light: #a2a2a2; --grey-dark: #5c5c5c;
  }
  * { margin: 0; padding: 0; box-sizing: border-box; }
  html, body { width: 1200px; height: 900px; overflow: hidden; background: var(--page); }
  body { position: relative; font-family: "Archivo", Arial, sans-serif; }

  .banner {
    position: absolute; left: 115px; width: 969px; height: 119px;
    border: 1px solid var(--frame); overflow: hidden; text-decoration: none;
    background: radial-gradient(ellipse 60% 90% at 50% 50%, var(--tone-light), var(--tone-dark));
  }
  .banner--red { top: 53px; --tone-light: var(--red-light); --tone-dark: var(--red-dark); }
  .banner--teal { top: 224px; --tone-light: var(--teal-light); --tone-dark: var(--teal-dark); }
  .banner--green { top: 393px; --tone-light: var(--green-light); --tone-dark: var(--green-dark); }
  .banner--purple { top: 564px; --tone-light: var(--purple-light); --tone-dark: var(--purple-dark); }
  .banner--grey { top: 733px; --tone-light: var(--grey-light); --tone-dark: var(--grey-dark); }

  .corner-panel { position: absolute; left: 0; top: 0; width: 130px; height: 119px; }
  .powered-by { position: absolute; left: 9px; top: 68px; font-size: 11px; font-style: italic; color: var(--powered); }
  .partner { position: absolute; left: 9px; top: 87px; display: flex; align-items: center; gap: 5px;
    font-size: 15px; font-style: italic; font-weight: 400; color: var(--brand-text); }
  .partner-dot { width: 18px; height: 18px; border-radius: 50%; background: var(--brand-dot); }

  .headline { position: absolute; left: 140px; top: 7px; font-style: italic; white-space: nowrap; }
  .headline-lead, .headline-tail { font-size: 20px; font-weight: 700; color: var(--ink); letter-spacing: 1px; }
  .headline-lead { word-spacing: 6px; }
  .headline-key { font-size: 27px; font-weight: 900; color: var(--white); margin: 0 6px 0 4px; }

  .products { position: absolute; left: 228px; top: 37px; list-style: none; font-style: italic; }
  .products li { height: 24px; display: flex; align-items: center; font-size: 17px; color: var(--ink); white-space: nowrap; }
  .products .arrow { width: 16px; height: 14px; margin-right: 6px; }
  .products b { font-weight: 900; letter-spacing: 2px; margin-right: 7px; }
  .products span { font-weight: 500; letter-spacing: 2px; }

  .cta { position: absolute; left: 544px; top: 42px; width: 190px; height: 44px;
    border: 2px dashed rgba(0,0,0,0.55); border-radius: 9px;
    display: flex; align-items: center; justify-content: center;
    font-size: 25px; font-weight: 900; font-style: italic; color: var(--white);
    text-shadow: 0 1px 1px rgba(0,0,0,0.35); }

  .house-illustration { position: absolute; left: 768px; top: 8px; width: 188px; height: 104px;
    border-radius: 4px; background: linear-gradient(180deg, rgba(0,0,0,0.10), rgba(0,0,0,0.26)); }
</style>
</head>
<body>

<a class="banner banner--red" href="https://www.telvan.com.au">
  <svg class="corner-panel" viewBox="0 0 130 119"><path d="M0,46 C62,40 114,62 126,119 L0,119 Z" fill="#fff"/></svg>
  <div class="powered-by">Powered by</div>
  <div class="partner"><i class="partner-dot"></i>Quotewell</div>
  <p class="headline"><span class="headline-lead">For An</span><span class="headline-key">INSTANT QUOTE</span><span class="headline-tail">On</span></p>
  <ul class="products">
    <li><svg class="arrow" viewBox="0 0 16 14"><path d="M0,5 H8 V0 L16,7 L8,14 V9 H0 Z" fill="#fff"/></svg><b>LIFE</b><span>Insurance</span></li>
    <li><svg class="arrow" viewBox="0 0 16 14"><path d="M0,5 H8 V0 L16,7 L8,14 V9 H0 Z" fill="#fff"/></svg><b>TPD</b><span>Insurance</span></li>
    <li><svg class="arrow" viewBox="0 0 16 14"><path d="M0,5 H8 V0 L16,7 L8,14 V9 H0 Z" fill="#fff"/></svg><b>INCOME</b><span>Protection</span></li>
  </ul>
  <span class="cta">CLICK HERE</span>
  <div class="house-illustration" role="img" aria-label="Line drawing of a two-storey family house with garage"></div>
</a>

<a class="banner banner--teal" href="https://www.telvan.com.au">
  <svg class="corner-panel" viewBox="0 0 130 119"><path d="M0,46 C62,40 114,62 126,119 L0,119 Z" fill="#fff"/></svg>
  <div class="powered-by">Powered by</div>
  <div class="partner"><i class="partner-dot"></i>Quotewell</div>
  <p class="headline"><span class="headline-lead">For An</span><span class="headline-key">INSTANT QUOTE</span><span class="headline-tail">On</span></p>
  <ul class="products">
    <li><svg class="arrow" viewBox="0 0 16 14"><path d="M0,5 H8 V0 L16,7 L8,14 V9 H0 Z" fill="#fff"/></svg><b>LIFE</b><span>Insurance</span></li>
    <li><svg class="arrow" viewBox="0 0 16 14"><path d="M0,5 H8 V0 L16,7 L8,14 V9 H0 Z" fill="#fff"/></svg><b>TPD</b><span>Insurance</span></li>
    <li><svg class="arrow" viewBox="0 0 16 14"><path d="M0,5 H8 V0 L16,7 L8,14 V9 H0 Z" fill="#fff"/></svg><b>INCOME</b><span>Protection</span></li>
  </ul>
  <span class="cta">CLICK HERE</span>
  <div class="house-illustration" role="img" aria-label="Line drawing of a two-storey family house with garage"></div>
</a>

<a class="banner banner--green" href="https://www.telvan.com.au">
  <svg class="corner-panel" viewBox="0 0 130 119"><path d="M0,46 C62,40 114,62 126,119 L0,119 Z" fill="#fff"/></svg>
  <div class="powered-by">Powered by</div>
  <div class="partner"><i class="partner-dot"></i>Quotewell</div>
  <p class="headline"><span class="headline-lead">For An</span><span class="headline-key">INSTANT QUOTE</span><span class="headline-tail">On</span></p>
  <ul class="products">
    <li><svg class="arrow" viewBox="0 0 16 14"><path d="M0,5 H8 V0 L16,7 L8,14 V9 H0 Z" fill="#fff"/></svg><b>LIFE</b><span>Insurance</span></li>
    <li><svg class="arrow" viewBox="0 0 16 14"><path d="M0,5 H8 V0 L16,7 L8,14 V9 H0 Z" fill="#fff"/></svg><b>TPD</b><span>Insurance</span></li>
    <li><svg class="arrow" viewBox="0 0 16 14"><path d="M0,5 H8 V0 L16,7 L8,14 V9 H0 Z" fill="#fff"/></svg><b>INCOME</b><span>Protection</span></li>
  </ul>
  <span class="cta">CLICK HERE</span>
  <div class="house-illustration" role="img" aria-label="Line drawing of a two-storey family house with garage"></div>
</a>

<a class="banner banner--purple" href="https://www.telvan.com.au">
  <svg class="corner-panel" viewBox="0 0 130 119"><path d="M0,46 C62,40 114,62 126,119 L0,119 Z" fill="#fff"/></svg>
  <div class="powered-by">Powered by</div>
  <div class="partner"><i class="partner-dot"></i>Quotewell</div>
  <p class="headline"><span class="headline-lead">For An</span><span class="headline-key">INSTANT QUOTE</span><span class="headline-tail">On</span></p>
  <ul class="products">
    <li><svg class="arrow" viewBox="0 0 16 14"><path d="M0,5 H8 V0 L16,7 L8,14 V9 H0 Z" fill="#fff"/></svg><b>LIFE</b><span>Insurance</span></li>
    <li><svg class="arrow" viewBox="0 0 16 14"><path d="M0,5 H8 V0 L16,7 L8,14 V9 H0 Z" fill="#fff"/></svg><b>TPD</b><span>Insurance</span></li>
    <li><svg class="arrow" viewBox="0 0 16 14"><path d="M0,5 H8 V0 L16,7 L8,14 V9 H0 Z" fill="#fff"/></svg><b>INCOME</b><span>Protection</span></li>
  </ul>
  <span class="cta">CLICK HERE</span>
  <div class="house-illustration" role="img" aria-label="Line drawing of a two-storey family house with garage"></div>
</a>

<a class="banner banner--grey" href="https://www.telvan.com.au">
  <svg class="corner-panel" viewBox="0 0 130 119"><path d="M0,46 C62,40 114,62 126,119 L0,119 Z" fill="#fff"/></svg>
  <div class="powered-by">Powered by</div>
  <div class="partner"><i class="partner-dot"></i>Quotewell</div>
  <p class="headline"><span class="headline-lead">For An</span><span class="headline-key">INSTANT QUOTE</span><span class="headline-tail">On</span></p>
  <ul class="products">
    <li><svg class="arrow" viewBox="0 0 16 14"><path d="M0,5 H8 V0 L16,7 L8,14 V9 H0 Z" fill="#fff"/></svg><b>LIFE</b><span>Insurance</span></li>
    <li><svg class="arrow" viewBox="0 0 16 14"><path d="M0,5 H8 V0 L16,7 L8,14 V9 H0 Z" fill="#fff"/></svg><b>TPD</b><span>Insurance</span></li>
    <li><svg class="arrow" viewBox="0 0 16 14"><path d="M0,5 H8 V0 L16,7 L8,14 V9 H0 Z" fill="#fff"/></svg><b>INCOME</b><span>Protection</span></li>
  </ul>
  <span class="cta">CLICK HERE</span>
  <div class="house-illustration" role="img" aria-label="Line drawing of a two-storey family house with garage"></div>
</a>

</body>
</html>
```